Gutschein-Design für Friseursalon gesucht
Zielgruppe
Wir sind ein Friseursalon für Jung bis Alt.
Wir bieten alles rund um das Haar an und verkaufen Haarpflegeprodukte.
Aufgabenstellung
Das Design sollte Modern und Professionell wirken.
Ebenso muss es zu unserem Firmenlogo passen.
Es sollte auf die Rückseite des Gutscheins ein Feld für den Betrag, für Wen, das Datum, den Stempel und die Gutscheinnummer vorhanden sein.

```html
<!DOCTYPE html>
<html lang="de">
<head>
<meta charset="utf-8">
<title>Gutschein – Lockenstudio by Veri</title>
<link rel="stylesheet" href="https://fonts.googleapis.com/css2?family=Arimo:ital,wght@0,400;0,500;1,400&display=swap">
<style>
  :root {
    --page: #ffffff;
    --card: #ece8ec;
    --card-light: #f7f5f7;
    --plum: #8b2a8c;
    --ink: #1e1e22;
    --photo-dark: #8e8a8e;
    --photo-mid: #c9c4c8;
    --photo-light: #e9e5e9;
  }
  * { margin: 0; padding: 0; box-sizing: border-box; }
  html, body { width: 1200px; height: 1200px; overflow: hidden; background: var(--page); }
  body { position: relative; font-family: "Arimo", Arial, sans-serif; color: var(--ink); }

  .voucher {
    position: absolute; left: 90px; width: 1043px; height: 487px;
    background: radial-gradient(ellipse at 35% 50%, var(--card-light), var(--card) 75%);
    box-shadow: 3px 4px 8px rgba(0,0,0,.25);
    overflow: hidden;
  }
  .voucher--front { top: 88px; }
  .voucher--back { top: 664px; }

  .frame {
    position: absolute; left: 54px; top: 54px; width: 934px; height: 381px;
    border: 2px solid var(--plum);
  }

  .photo { position: absolute; top: 0; height: 100%; }
  .voucher--front .photo {
    left: 455px; width: 588px;
    background:
      linear-gradient(90deg, var(--card) 0%, rgba(236,232,236,0) 30%),
      radial-gradient(ellipse at 62% 42%, var(--photo-light) 0%, var(--photo-mid) 45%, var(--photo-dark) 80%, var(--photo-mid) 100%);
  }
  .voucher--back .photo {
    left: 582px; width: 461px;
    background:
      linear-gradient(135deg, var(--photo-dark) 0%, var(--photo-mid) 35%, var(--photo-light) 65%, var(--card-light) 100%);
  }

  .brand { position: absolute; text-align: right; line-height: 1; }
  .brand__name { display: block; font-weight: 400; color: var(--ink); }
  .brand__sub { display: block; color: var(--plum); }
  .voucher--front .brand { left: 80px; top: 210px; }
  .voucher--front .brand__name { font-size: 50px; }
  .voucher--front .brand__sub { font-size: 24px; margin-top: 8px; }
  .voucher--back .brand { left: 712px; top: 205px; }
  .voucher--back .brand__name { font-size: 30px; }
  .voucher--back .brand__sub { font-size: 15px; margin-top: 4px; }

  .title {
    position: absolute; left: 510px; top: 344px;
    font-size: 74px; font-weight: 400; letter-spacing: 1px; color: var(--plum);
  }

  .field { position: absolute; display: flex; align-items: flex-end; font-style: italic; color: var(--plum); }
  .field__line { border-bottom: 2px solid var(--plum); margin-left: 14px; margin-bottom: 4px; }
  .field--amount { left: 70px; top: 104px; font-size: 23px; }
  .field--amount .field__line { width: 386px; }
  .field--for { left: 70px; top: 189px; font-size: 23px; }
  .field--for .field__line { width: 436px; }
  .field--number { left: 228px; top: 264px; font-size: 16px; }
  .field--number .field__line { width: 147px; margin-bottom: 2px; }
  .field--date { left: 70px; top: 398px; font-size: 16px; }
  .field--date .field__line { width: 162px; margin-bottom: 2px; }
  .field--stamp { left: 314px; top: 398px; font-size: 16px; }
  .field--stamp .field__line { width: 170px; margin-bottom: 2px; }

  .contact {
    position: absolute; left: 672px; top: 318px; width: 312px;
    text-align: center; font-style: italic; font-size: 17.5px; line-height: 24px; color: var(--ink);
  }
  .contact__owner { font-size: 24px; color: var(--plum); line-height: 28px; }
</style>
</head>
<body>

  <section class="voucher voucher--front">
    <div class="photo" role="img" aria-label="Schwarz-Weiß-Porträtfoto einer blonden Frau mit violettem Augen-Make-up"></div>
    <div class="frame"></div>
    <div class="brand">
      <span class="brand__name">Lockenstudio</span>
      <span class="brand__sub">by Veri</span>
    </div>
    <h1 class="title">GUTSCHEIN</h1>
  </section>

  <section class="voucher voucher--back">
    <div class="photo" role="img" aria-label="Halbes Porträtfoto einer blonden Frau, oben rechts eine violette Geschenkschleife"></div>
    <div class="frame"></div>

    <div class="field field--amount"><span>BETRAG</span><span class="field__line"></span></div>
    <div class="field field--for"><span>FÜR</span><span class="field__line"></span></div>
    <div class="field field--number"><span>GUTSCHEINNUMMER</span><span class="field__line"></span></div>
    <div class="field field--date"><span>DATUM</span><span class="field__line"></span></div>
    <div class="field field--stamp"><span>STEMPEL</span><span class="field__line"></span></div>

    <div class="brand">
      <span class="brand__name">Lockenstudio</span>
      <span class="brand__sub">by Veri</span>
    </div>

    <address class="contact">
      <div>Inhaberin Friseurmeisterin</div>
      <div class="contact__owner">Veri Sonnfeld</div>
      <div>Lindenweg 8 &nbsp;•&nbsp; 5420 Feldhain</div>
      <div>Telefon: 06571/4820</div>
    </address>
  </section>

</body>
</html>
```